Horrorautorin sucht Buch-Cover
Zielgruppe
Ich bin Horrorautorin.
Zielgruppe: Männer und Frauen von 18 bis 60 Jahren.
Aufgabenstellung
Auf die Vorderseite und den Buchrücken müssten die Informationen:
Titel: Der Nachtweber
Autor: Mira Boltek
Auf die Rückseite kommt der Klappentext, den ich nach Coverauswahl nachreiche.
Ich suche ein stilvolles Cover am liebsten ohne die typischen Blutspritzer. Die Schrift soll zum Horrorgenre passen. Es soll hübsch und gleichzeitig düster sein.
Bitte keine schreienden Menschen oder Hände mit einem Messer etc.
Generell mag ich es nicht, wenn Menschen / Gesichter auf den Covern zu sehen sind. In Ordnung sind schemenhafte Umrisse oder Schatten von Personen.
Atmosphäre/Stimmung: Düster, gruselig, am besten angsteinflößend und bedrohlich. Die Geschichte enthält heftige, explizite Gewaltdarstellungen.
Zum Inhalt des Romans:
Dem Horrorautor Rupert Olden (= Der Nachtweber) genügt es nicht mehr, mit seinen Gruselgeschichten den Lesern Angst einzujagen. Daher lädt er zu einem Horrorabend ein, wie ihn niemand erwartet hätte. Seine Gäste müssen ein Spiel um Leben und Tod überstehen, das sie nur gewinnen können, wenn sie die eigenen Grenzen überschreiten. Angst, Ekel und Schmerz stehen auf Ruperts Speiseplan und er wird viel davon bekommen.
Das Setting ist England in der Gegenwart angesiedelt. Die Haupthandlung des Romans spielt in einer Villa im Wald (im Herbst). Sie ist nicht verfallen. Aber eine Villa im Wald auf dem Cover weckt vielleicht falsche Genreerwartungen.
Eine Vorlage für das richtige Layout (bzgl. Seitenzahl etc.) habe ich hochgeladen.
Damit Sie sich einen Eindruck von meinem Geschmack machen können, hier ein Link vom Lieblingscover meiner Bücher:
http://lnkvo.to/7Kq9xWb

```html
<!DOCTYPE html>
<html lang="de">
<head>
<meta charset="utf-8">
<title>Der Nachtweber – Buchumschlag</title>
<link rel="stylesheet" href="https://fonts.googleapis.com/css2?family=Bebas+Neue&family=Anton&family=Playfair+Display:wght@400&display=swap">
<style>
  :root {
    --ink: #0b0b0b;
    --paper: #ececec;
    --blood: #c71a1a;
    --ash: #f6e6e0;
    --smoke: #e8a995;
    --text: #111111;
  }
  * { margin: 0; padding: 0; box-sizing: border-box; }
  html, body { width: 1200px; height: 879px; overflow: hidden; background: var(--ink); }
  .wrap { position: relative; width: 1200px; height: 879px; overflow: hidden; }
  .fx-defs { position: absolute; width: 0; height: 0; }
  .distressed { filter: url(#grunge); }

  /* Back cover */
  .back { position: absolute; left: 0; top: 0; width: 575px; height: 879px; background: var(--paper); }
  .back-art { position: absolute; inset: 0; }
  .back-title { position: absolute; left: 0; width: 575px; top: 138px; text-align: center;
    font-family: "Bebas Neue", "Oswald", sans-serif; font-weight: 400; color: var(--blood); line-height: 0.9; }
  .back-title .kicker { display: block; font-size: 33px; }
  .back-title .main { display: block; font-size: 60px; letter-spacing: 0.5px; }
  .blurb { position: absolute; left: 101px; top: 249px; width: 370px;
    font-family: "Playfair Display", Georgia, serif; font-size: 16.4px; line-height: 21.3px;
    color: var(--text); text-align: justify; }
  .blurb p + p { margin-top: 21.3px; }

  /* Spine */
  .spine { position: absolute; left: 575px; top: 0; width: 53px; height: 879px; background: var(--ink); }
  .spine-text { position: absolute; left: 50%; white-space: nowrap; transform-origin: left top;
    font-family: "Bebas Neue", "Oswald", sans-serif; line-height: 1; }
  .spine-author { top: 80px; color: var(--ash); font-size: 46px; transform: translateX(23px) rotate(90deg); letter-spacing: 1px; }
  .spine-title { top: 506px; color: var(--blood); font-size: 52px; transform: translateX(25px) rotate(90deg); letter-spacing: 1px; }

  /* Front cover */
  .front { position: absolute; left: 628px; top: 0; width: 572px; height: 879px; background: var(--ink); }
  .front-scene { position: absolute; inset: 0; width: 572px; height: 879px; }
  .front-title { position: absolute; left: 0; width: 572px; top: 58px; text-align: center;
    font-family: "Bebas Neue", "Oswald", sans-serif; font-weight: 400; color: var(--blood); line-height: 0.86; }
  .front-title .kicker { display: block; font-size: 66px; }
  .front-title .main { display: block; font-size: 118px; letter-spacing: 1px; }
  .front-author { position: absolute; left: 0; width: 572px; top: 728px; text-align: center;
    font-family: "Anton", "Impact", sans-serif; font-size: 90px; line-height: 1.1; color: var(--ash);
    letter-spacing: 5px; word-spacing: 22px; }
</style>
</head>
<body>
<svg class="fx-defs" aria-hidden="true">
  <filter id="grunge" x="0" y="0" width="100%" height="100%">
    <feTurbulence type="fractalNoise" baseFrequency="0.85" numOctaves="2" seed="7" result="noise"/>
    <feColorMatrix in="noise" type="matrix" values="0 0 0 0 0  0 0 0 0 0  0 0 0 0 0  -5.5 0 0 0 4.2" result="mask"/>
    <feComposite in="SourceGraphic" in2="mask" operator="in"/>
  </filter>
</svg>
<main class="wrap">
  <section class="back">
    <svg class="back-art" width="575" height="879" viewBox="0 0 575 879" role="img" aria-label="Symmetrisches Rauch-Klecksbild mit Schädelformen in Rot und Weiß, durchzogen von hellen Lichtbahnen">
      <defs>
        <radialGradient id="smokeGlow" cx="50%" cy="45%" r="65%">
          <stop offset="0" stop-color="#f2f0ef"/>
          <stop offset="1" stop-color="#e3e1e0"/>
        </radialGradient>
        <linearGradient id="smokeTop" x1="0" y1="0" x2="0" y2="1">
          <stop offset="0" stop-color="#e9a48f"/>
          <stop offset="1" stop-color="#2a1512"/>
        </linearGradient>
        <linearGradient id="smokeBottom" x1="0" y1="0" x2="0" y2="1">
          <stop offset="0" stop-color="#3a1a14"/>
          <stop offset="0.5" stop-color="#d98d78"/>
          <stop offset="1" stop-color="#f2d2c6"/>
        </linearGradient>
      </defs>
      <rect width="575" height="879" fill="url(#smokeGlow)"/>
      <rect x="0" y="0" width="575" height="120" fill="url(#smokeTop)"/>
      <polygon points="0,0 575,0 575,120 0,110" fill="#161010" opacity="0.55"/>
      <polygon points="0,110 230,66 575,96 575,126 0,126" fill="url(#smokeGlow)"/>
      <polygon points="230,66 575,20 575,98" fill="#eeeeee"/>
      <polygon points="228,68 575,98 575,126" fill="#111"/>
      <polygon points="0,632 575,760 575,790 0,660" fill="#111"/>
      <polygon points="0,685 575,880 575,879 0,720" fill="#111"/>
      <rect x="0" y="760" width="575" height="119" fill="url(#smokeBottom)" opacity="0.85"/>
      <polygon points="0,660 575,790 575,835 0,685" fill="#efefef"/>
      <polygon points="0,720 575,879 430,879 0,760" fill="#f1e3de" opacity="0.8"/>
    </svg>
    <h2 class="back-title distressed"><span class="kicker">Der</span><span class="main">Nachtweber</span></h2>
    <div class="blurb">
      <p>HIER KOMMT DER KLAPPENTEXT HIN.<br>Dem Horrorautor Rupert Olden (= der Nachtweber) genügt es nicht mehr, mit seinen Gruselgeschichten den Lesern Angst einzujagen. Daher lädt er zu einem Horrorabend ein, wie ihn niemand erwartet hätte. Seine Gäste müssen ein Spiel um Leben und Tod überstehen, das sie nur gewinnen können, wenn sie die eigenen Grenzen überschreiten. Angst, Ekel und Schmerz stehen auf Ruperts Speiseplan und er wird viel davon bekommen.</p>
      <p>Das Setting ist England in der Gegenwart angesiedelt. Die Haupthandlung des Romans spielt in einer Villa im Wald (im Herbst). Sie ist nicht verfallen. Aber eine Villa im Wald auf dem Cover weckt vielleicht falsche Genreerwartungen.</p>
    </div>
  </section>

  <section class="spine">
    <span class="spine-text spine-author distressed">Mira Boltek</span>
    <span class="spine-text spine-title distressed">Der Nachtweber</span>
  </section>

  <section class="front">
    <svg class="front-scene" width="572" height="879" viewBox="0 0 572 879" role="img" aria-label="Silhouette einer Villa mit rot leuchtenden Fenstern zwischen kahlen Bäumen vor hellem, rötlich verrauchtem Himmel">
      <defs>
        <linearGradient id="sky" x1="0" y1="0" x2="0" y2="1">
          <stop offset="0" stop-color="#f8f2f0"/>
          <stop offset="0.25" stop-color="#f6f3f2"/>
          <stop offset="0.38" stop-color="#f1e9e6"/>
          <stop offset="0.47" stop-color="#e6c6bb"/>
          <stop offset="0.55" stop-color="#5a2e26"/>
          <stop offset="0.63" stop-color="#0a0606"/>
          <stop offset="1" stop-color="#000"/>
        </linearGradient>
        <radialGradient id="moon" cx="52%" cy="30%" r="35%">
          <stop offset="0" stop-color="#ffffff" stop-opacity="0.95"/>
          <stop offset="1" stop-color="#ffffff" stop-opacity="0"/>
        </radialGradient>
        <linearGradient id="leftTrees" x1="0" y1="0" x2="1" y2="0">
          <stop offset="0" stop-color="#0b0606" stop-opacity="0.75"/>
          <stop offset="1" stop-color="#0b0606" stop-opacity="0"/>
        </linearGradient>
        <linearGradient id="rightTrees" x1="1" y1="0" x2="0" y2="0">
          <stop offset="0" stop-color="#0b0606" stop-opacity="0.7"/>
          <stop offset="1" stop-color="#0b0606" stop-opacity="0"/>
        </linearGradient>
        <radialGradient id="glow" cx="50%" cy="50%" r="50%">
          <stop offset="0" stop-color="#c7452f" stop-opacity="0.55"/>
          <stop offset="1" stop-color="#c7452f" stop-opacity="0"/>
        </radialGradient>
      </defs>
      <rect width="572" height="879" fill="url(#sky)"/>
      <rect width="572" height="879" fill="url(#moon)"/>
      <rect x="0" y="200" width="160" height="360" fill="url(#leftTrees)"/>
      <rect x="380" y="220" width="192" height="340" fill="url(#rightTrees)"/>
      <ellipse cx="330" cy="470" rx="220" ry="70" fill="url(#glow)"/>
    </svg>
    <h1 class="front-title distressed"><span class="kicker">Der</span><span class="main">Nachtweber</span></h1>
    <p class="front-author distressed">MIRA BOLTEK</p>
  </section>
</main>
</body>
</html>
```